Ferncrest Dental, LLC business card project

Business card to be designed with current logo.
Dental office- please keep design of card that looks clean and professional.
Please include the following info:
Ferncrest Dental, LLC
Dr. Lorna Pettigrew
2871 Marlowe Street
Bethlehem, PA 18093
610-555-0193
ferncrestdental.office@examplemail.test
Hello everyone-
Reason: Just got back from overseas- will look at all designs and provide feedback. Thank you!
Reason: Polling my friends for the final selection-
thank you to all those that participated- so many talented designers!

```html
<!DOCTYPE html>
<html lang="en">
<head>
<meta charset="utf-8">
<title>Ferncrest Dental, LLC – Business Card</title>
<link rel="stylesheet" href="https://fonts.googleapis.com/css2?family=Questrial&display=swap">
<style>
  :root {
    --page-bg: #e9ecee;
    --card-white: #ffffff;
    --leaf-green: #65a243;
    --lime: #b3d235;
    --brand-green: #4f8f37;
    --text-white: #ffffff;
    --card-shadow: rgba(30, 45, 50, 0.18);
  }
  * { box-sizing: border-box; margin: 0; padding: 0; }
  html, body {
    width: 1200px;
    height: 960px;
    overflow: hidden;
    background: var(--page-bg);
    font-family: "Questrial", "Century Gothic", sans-serif;
  }
  .sheet {
    width: 1200px;
    height: 960px;
    display: flex;
    flex-direction: column;
    align-items: center;
    justify-content: center;
    gap: 40px;
  }
  .card {
    position: relative;
    width: 700px;
    height: 400px;
    overflow: hidden;
    box-shadow: 0 10px 30px var(--card-shadow);
  }

  /* Front */
  .card--front { background: var(--card-white); }
  .card__wave {
    position: absolute;
    inset: 0;
    width: 100%;
    height: 100%;
  }
  .brand {
    position: absolute;
    top: 78px;
    left: 0;
    right: 0;
    display: flex;
    align-items: center;
    justify-content: center;
    gap: 18px;
  }
  .brand__dot {
    width: 44px;
    height: 44px;
    border-radius: 50%;
    background: var(--lime);
  }
  .brand__name {
    font-size: 52px;
    color: var(--brand-green);
    letter-spacing: -0.5px;
  }
  .holder {
    position: absolute;
    top: 246px;
    left: 0;
    right: 0;
    text-align: center;
    font-size: 27px;
    color: var(--text-white);
  }
  .contact {
    position: absolute;
    top: 298px;
    left: 0;
    right: 0;
    display: flex;
    flex-direction: column;
    align-items: center;
    gap: 12px;
    color: var(--text-white);
    font-size: 17px;
  }
  .contact__row {
    display: flex;
    align-items: center;
    gap: 26px;
  }
  .contact__item {
    display: flex;
    align-items: center;
    gap: 10px;
  }
  .contact__icon {
    width: 16px;
    height: 16px;
    fill: var(--text-white);
  }

  /* Back */
  .card--back {
    background: var(--leaf-green);
    display: flex;
    align-items: center;
    justify-content: center;
    gap: 18px;
  }
  .card--back .brand__name { color: var(--text-white); }
  .card--back .brand__dot { background: var(--lime); }
</style>
</head>
<body>
<main class="sheet">

  <section class="card card--front" aria-label="Business card front">
    <svg class="card__wave" viewBox="0 0 700 400" preserveAspectRatio="none" aria-hidden="true">
      <path d="M0 238 Q 330 170 700 178 L700 400 L0 400 Z" fill="var(--lime)"/>
      <path d="M0 250 Q 330 182 700 190 L700 400 L0 400 Z" fill="var(--card-white)"/>
      <path d="M0 258 Q 330 190 700 198 L700 400 L0 400 Z" fill="var(--leaf-green)"/>
    </svg>

    <div class="brand">
      <span class="brand__dot"></span>
      <span class="brand__name">Ferncrest Dental</span>
    </div>

    <p class="holder">Dr. Lorna Pettigrew</p>

    <div class="contact">
      <div class="contact__row">
        <span class="contact__item">
          <svg class="contact__icon" viewBox="0 0 24 24" aria-hidden="true">
            <path d="M6.6 10.8a15.1 15.1 0 0 0 6.6 6.6l2.2-2.2a1 1 0 0 1 1-.25 11.4 11.4 0 0 0 3.6.57 1 1 0 0 1 1 1V20a1 1 0 0 1-1 1A17 17 0 0 1 3 4a1 1 0 0 1 1-1h3.5a1 1 0 0 1 1 1c0 1.25.2 2.45.57 3.6a1 1 0 0 1-.25 1z"/>
          </svg>
          610-555-0193
        </span>
        <span class="contact__item">
          <svg class="contact__icon" viewBox="0 0 24 24" aria-hidden="true">
            <path d="M2 5h20v14H2z M4 7v.5l8 5.5 8-5.5V7l-8 5.5z" fill-rule="evenodd"/>
          </svg>
          ferncrestdental.office@examplemail.test
        </span>
      </div>
      <div class="contact__row">
        <span class="contact__item">
          <svg class="contact__icon" viewBox="0 0 24 24" aria-hidden="true">
            <path d="M12 2a7 7 0 0 0-7 7c0 5.2 7 13 7 13s7-7.8 7-13a7 7 0 0 0-7-7zm0 9.5A2.5 2.5 0 1 1 12 6.5a2.5 2.5 0 0 1 0 5z"/>
          </svg>
          2871 Marlowe Street, Bethlehem, PA 18093
        </span>
      </div>
    </div>
  </section>

  <section class="card card--back" aria-label="Business card back">
    <span class="brand__dot"></span>
    <span class="brand__name">Ferncrest Dental</span>
  </section>

</main>
</body>
</html>
```